Marrow Business Cards

Front of business card will have logo, name, address, & telephone number. Back of card will have a list of services provided - Roads, Substation Pads, Temporary Pads, Site Pads, Land Leveling, Powerline Row Cleaning, Land Clearing, Gates, Fencing, Construction Entrances, Excavation, Trenching, Underground Utilities, Directional Boring, Pile Driving. We are a construction company that uses heavy equipment like bulldozers, motor graders/blades, dump trucks, backhoes, hydro axes, & skid loaders. We build roads, pads, & install electric utility lines & waterlines underground. This logo is new. The word "Construction" can be smaller as uploaded 2 example edited logos. We will be using this card design for many employees.
Target Market(s)
Industrial Electric Powerline, Wind Turbine, Solar Panel, & Water Utility companies.
Contact Information for Business Card
Name/Position - Dorian Quale - Owner
Address: 4837 FM 582
Harlow, OK 73418
Phone number - (405) 418-2906

```html
<!DOCTYPE html>
<html lang="en">
<head>
<meta charset="UTF-8">
<title>Marrow Construction – Business Cards</title>
<link href="https://fonts.googleapis.com/css2?family=Lato:wght@400;700;900&display=swap" rel="stylesheet">
<style>
  :root {
    --maroon: #3d111c;
    --white: #ffffff;
    --grey: #6b6b6b;
    --stripe: #6a6a6a;
    --backdrop-top: #6e7074;
    --backdrop-bottom: #2a2b2e;
  }
  html, body {
    margin: 0;
    padding: 0;
    width: 1200px;
    height: 900px;
    overflow: hidden;
  }
  body {
    background: linear-gradient(160deg, var(--backdrop-top), var(--backdrop-bottom));
    font-family: "Lato", sans-serif;
    position: relative;
  }
  .card {
    position: absolute;
    width: 560px;
    height: 320px;
    border-radius: 26px;
    overflow: hidden;
    box-shadow: 0 12px 30px rgba(0,0,0,0.45);
  }
  /* Back of card: services */
  .card-back {
    left: 70px;
    top: 110px;
    background: var(--maroon);
    color: var(--white);
  }
  .wordmark {
    position: absolute;
    font-family: "Lato", sans-serif;
    font-weight: 700;
    text-align: center;
    line-height: 1;
    text-transform: uppercase;
  }
  .card-back .wordmark {
    left: 0;
    right: 0;
    top: 62px;
    color: var(--white);
  }
  .wordmark-main { display: block; font-size: 44px; letter-spacing: 6px; }
  .wordmark-sub { display: block; font-size: 26px; letter-spacing: 2px; margin-top: 8px; }
  .services {
    position: absolute;
    left: 10px;
    right: 10px;
    top: 196px;
    margin: 0;
    text-align: center;
    font-size: 13px;
    line-height: 1.9;
    white-space: nowrap;
  }
  .services .sep { margin: 0 5px; }

  /* Front of card: contact */
  .card-front {
    left: 570px;
    top: 470px;
    background: var(--white);
  }
  .card-front .wave {
    position: absolute;
    inset: 0;
  }
  .card-front .wordmark {
    right: 40px;
    top: 40px;
    color: var(--maroon);
  }
  .card-front .wordmark-main { font-size: 40px; }
  .card-front .wordmark-sub { font-size: 23px; }
  .person {
    position: absolute;
    left: 40px;
    top: 110px;
  }
  .person-name {
    margin: 0;
    font-size: 30px;
    font-weight: 900;
    color: var(--maroon);
  }
  .person-role {
    margin: 4px 0 0 36px;
    font-size: 16px;
    color: var(--grey);
  }
  .contact {
    position: absolute;
    left: 170px;
    top: 200px;
    color: var(--white);
    font-size: 15px;
    line-height: 19px;
  }
  .contact p { margin: 0; }
  .contact .address { margin-bottom: 5px; }
  .contact-row {
    display: flex;
    align-items: center;
    gap: 10px;
  }
  .contact-row svg { width: 14px; height: 14px; flex: none; }
</style>
</head>
<body>

  <section class="card card-back" aria-label="Business card back">
    <div class="wordmark">
      <span class="wordmark-main">Marrow</span>
      <span class="wordmark-sub">Construction</span>
    </div>
    <p class="services">
      Roads<span class="sep">|</span>Substation Pads<span class="sep">|</span>Temporary Pads<span class="sep">|</span>Site Pads<span class="sep">|</span>Land Leveling<br>
      Powerline Row Cleaning<span class="sep">|</span>Land Clearing<span class="sep">|</span>Gates<span class="sep">|</span>Fencing<span class="sep">|</span>Construction Entrances<br>
      Excavation<span class="sep">|</span>Trenching<span class="sep">|</span>Underground Utilities<span class="sep">|</span>Directional Boring<span class="sep">|</span>Pile Driving
    </p>
  </section>

  <section class="card card-front" aria-label="Business card front">
    <svg class="wave" viewBox="0 0 560 320" width="560" height="320" aria-hidden="true">
      <path d="M46,320 C54,200 130,152 310,148 C360,147 390,146 410,144" fill="none" stroke="var(--stripe)" stroke-width="9"/>
      <path d="M62,320 C70,212 146,166 326,160 C470,156 540,150 560,100 L560,320 Z" fill="var(--maroon)"/>
    </svg>

    <div class="wordmark">
      <span class="wordmark-main">Marrow</span>
      <span class="wordmark-sub">Construction</span>
    </div>

    <div class="person">
      <h1 class="person-name">Dorian Quale</h1>
      <p class="person-role">Owner</p>
    </div>

    <div class="contact">
      <p>4837 FM 582</p>
      <p class="address">Harlow, OK 73418</p>
      <p class="contact-row">
        <svg viewBox="0 0 16 16" aria-hidden="true"><path d="M3 1.5l2.5 0 1.2 3-1.5 1.2c.8 1.8 2.3 3.3 4.1 4.1l1.2-1.5 3 1.2v2.5c0 .8-.7 1.5-1.5 1.5C6.7 13.5 2.5 9.3 1.5 3c0-.8.7-1.5 1.5-1.5z" fill="var(--white)"/></svg>
        (405) 418-2906
      </p>
      <p class="contact-row">
        <svg viewBox="0 0 16 16" aria-hidden="true"><rect x="1" y="3.5" width="14" height="9" fill="none" stroke="var(--white)" stroke-width="1.4"/><path d="M1 3.5l7 5 7-5" fill="none" stroke="var(--white)" stroke-width="1.4"/></svg>
        info@marrowconstruction.com
      </p>
      <p class="contact-row">
        <svg viewBox="0 0 16 16" aria-hidden="true"><circle cx="8" cy="8" r="6.5" fill="none" stroke="var(--white)" stroke-width="1.3"/><ellipse cx="8" cy="8" rx="3" ry="6.5" fill="none" stroke="var(--white)" stroke-width="1.1"/><path d="M1.5 8h13" stroke="var(--white)" stroke-width="1.1"/></svg>
        www.marrowconstruction.com
      </p>
    </div>
  </section>

</body>
</html>
```